Keep Harbor Homes. Avoid short sale, foreclosure, repossession, negative credit inquires and all other negative actions associated with your real estate.

Call 844-27-LUMEN or info@keepharborhomes.example

```html
<!DOCTYPE html>
<html lang="en">
<head>
<meta charset="utf-8">
<title>Keep Harbor Homes – Postcard</title>
<link rel="stylesheet" href="https://fonts.googleapis.com/css2?family=Oswald:wght@500&family=Raleway:wght@600&family=Montserrat:wght@500&family=Source+Sans+3:ital,wght@1,400;1,600&display=swap">
<style>
  :root{
    --bg:#d9d9d9;
    --ink:#0b0b0c;
    --panel:#101113;
    --blue:#1d6db3;
    --blue-dark:#175c99;
    --brand-blue:#2277c6;
    --white:#ffffff;
    --rule:#9a9a9a;
    --rim:#c9cbce;
  }
  *{box-sizing:border-box;margin:0;padding:0}
  html,body{width:991px;height:1200px;overflow:hidden;background:var(--bg)}
  .postcard{position:absolute;left:116px;width:774px;height:525px;overflow:hidden;background:var(--white)}
  .postcard--front{top:53px}
  .postcard--back{top:626px}

  .photo{position:absolute}
  .front-photo{left:0;top:0;width:774px;height:360px;
    background:linear-gradient(120deg,#6f7a62 0%,#a89a88 35%,#c4b4a4 55%,#8c98a8 80%,#6b7e5a 100%)}
  .front-panel{position:absolute;left:0;top:0;width:774px;height:525px}
  .round-photo{position:absolute;width:144px;height:144px;border-radius:50%;border:6px solid var(--rim)}
  .round-photo--house{left:424px;top:239px;background:radial-gradient(circle at 50% 40%,#b7bfd6,#4d5572 75%)}
  .round-photo--deal{left:596px;top:239px;background:radial-gradient(circle at 50% 45%,#c99a7b,#6f7f5c 75%)}

  .headline{position:absolute;left:30px;line-height:1}
  .headline__top{display:block;font-family:'Raleway',sans-serif;font-weight:600;font-size:48px;letter-spacing:3px;color:var(--white)}
  .headline__main{display:block;font-family:'Oswald',sans-serif;font-weight:500;font-size:78px;color:var(--brand-blue);margin-top:4px}
  .front-headline{top:336px}
  .back-headline{top:30px}

  .tagline{position:absolute;font-family:'Source Sans 3',sans-serif;font-style:italic;color:var(--white)}
  .front-tagline{left:418px;top:396px;width:340px;font-size:15px;line-height:21px;font-weight:400}
  .back-tagline{left:32px;top:188px;width:360px;font-size:16px;line-height:21px;font-weight:600}

  .contact-bar{position:absolute;left:0;bottom:0;width:774px;height:57px;background:var(--blue)}
  .contact-bar__split{position:absolute;left:387px;top:0;width:387px;height:57px;background:var(--blue-dark)}
  .phone{position:absolute;left:32px;top:9px;display:flex;align-items:center;gap:14px;
    font-family:'Montserrat',sans-serif;font-weight:500;font-size:35px;color:var(--white)}
  .email{position:absolute;left:414px;top:15px;display:flex;align-items:center;gap:10px;
    font-family:'Montserrat',sans-serif;font-weight:500;font-size:19px;color:var(--white)}

  .back-panel{position:absolute;left:0;top:0;width:412px;height:468px}
  .dotted-rule{position:absolute;left:32px;top:171px;width:356px;border-top:2px dotted var(--white)}
  .back-photo{left:0;top:254px;width:388px;height:214px;
    background:linear-gradient(180deg,#101113 0%,#5b5148 40%,#8a8278 70%,#6d7a58 100%)}
  .stamp{position:absolute;left:647px;top:28px;width:104px;height:125px;border:1.5px solid var(--rule);
    font-family:'Montserrat',sans-serif;font-weight:500;font-size:14px;color:#444;text-align:center;padding-top:42px;line-height:19px}
  .address-line{position:absolute;left:446px;width:305px;border-top:1.5px solid var(--rule)}
</style>
</head>
<body>

<section class="postcard postcard--front">
  <div class="photo front-photo" role="img" aria-label="Photo of a couple embracing in front of a house with a foreclosure for-sale sign"></div>
  <svg class="front-panel" viewBox="0 0 774 525" aria-hidden="true">
    <polygon points="0,302 388,302 410,330 774,330 774,525 0,525" fill="#8c8f94"/>
    <polygon points="0,306 386,306 408,334 774,334 774,525 0,525" fill="var(--panel)"/>
  </svg>
  <div class="round-photo round-photo--house" role="img" aria-label="Photo of a lit suburban house at dusk"></div>
  <div class="round-photo round-photo--deal" role="img" aria-label="Photo of a handshake in front of a house"></div>

  <h1 class="headline front-headline">
    <span class="headline__top">KEEP HARBOR</span>
    <span class="headline__main">HOMES</span>
  </h1>
  <p class="tagline front-tagline">Avoid short sale, foreclosure, repossession, negative credit inquires and all other negative actions associated with your real estate.</p>

  <div class="contact-bar">
    <div class="contact-bar__split"></div>
    <div class="phone">
      <svg width="40" height="40" viewBox="0 0 40 40" aria-hidden="true"><circle cx="20" cy="20" r="17.5" fill="none" stroke="#fff" stroke-width="3"/><path d="M13 11c2-1 3 0 4 3l1 2c0 1-1 2-2 3 1 3 3 5 6 6 1-1 2-2 3-2l2 1c3 1 4 2 3 4-1 2-3 3-5 2-6-2-11-7-13-13-1-2 0-5 1-6z" fill="#fff"/></svg>
      <span>844-27-LUMEN</span>
    </div>
    <div class="email">
      <svg width="15" height="15" viewBox="0 0 15 15" aria-hidden="true"><circle cx="7.5" cy="7.5" r="6.5" fill="none" stroke="#fff" stroke-width="2"/><rect x="4" y="6.5" width="7" height="2" fill="#fff"/></svg>
      <span>info@keepharborhomes.example</span>
    </div>
  </div>
</section>

<section class="postcard postcard--back">
  <svg class="back-panel" viewBox="0 0 412 468" aria-hidden="true">
    <polygon points="0,0 412,0 412,256 392,276 392,468 0,468" fill="#8c8f94"/>
    <polygon points="0,0 408,0 408,254 388,274 388,468 0,468" fill="var(--panel)"/>
  </svg>
  <h2 class="headline back-headline">
    <span class="headline__top">KEEP HARBOR</span>
    <span class="headline__main">HOMES</span>
  </h2>
  <div class="dotted-rule"></div>
  <p class="tagline back-tagline">Avoid short sale, foreclosure, repossession, negative credit inquires and all other negative actions associated with your real estate.</p>
  <div class="photo back-photo" role="img" aria-label="Photo of a large brick house with a foreclosure house-for-sale sign on the lawn"></div>

  <div class="stamp">STAMP<br>HERE</div>
  <div class="address-line" style="top:257px"></div>
  <div class="address-line" style="top:315px"></div>
  <div class="address-line" style="top:373px"></div>
  <div class="address-line" style="top:430px"></div>

  <div class="contact-bar">
    <div class="contact-bar__split"></div>
    <div class="phone">
      <svg width="40" height="40" viewBox="0 0 40 40" aria-hidden="true"><circle cx="20" cy="20" r="17.5" fill="none" stroke="#fff" stroke-width="3"/><path d="M13 11c2-1 3 0 4 3l1 2c0 1-1 2-2 3 1 3 3 5 6 6 1-1 2-2 3-2l2 1c3 1 4 2 3 4-1 2-3 3-5 2-6-2-11-7-13-13-1-2 0-5 1-6z" fill="#fff"/></svg>
      <span>844-27-LUMEN</span>
    </div>
    <div class="email">
      <svg width="15" height="15" viewBox="0 0 15 15" aria-hidden="true"><circle cx="7.5" cy="7.5" r="6.5" fill="none" stroke="#fff" stroke-width="2"/><rect x="4" y="6.5" width="7" height="2" fill="#fff"/></svg>
      <span>info@keepharborhomes.example</span>
    </div>
  </div>
</section>

</body>
</html>
```